Business card for psychiatrist

Business card design project for a psychiatristWe would like to have the impression of 1. We (patient and the doctor) are working together.2. Light the way so that patients can see where they are going and what their goals are.3. One side of the business card will have the letter "BFP" which stands for Brynmoor Family Psychiatry.4. The other side of the business card will have the address, phone number, name of the psychiatrist, website, etc.5. A logo could go into either side of the business card. Let's see what looks better.
Business card design project for a psychiatrist
We would like to have the impression of
1. We (patient and the doctor) are working together.
2. Light the way so that patients can see where they are going and what their goals are.
3. One side of the business card will have the letter "BFP" which stands for Brynmoor Family Psychiatry.
4. The other side of the business card will have the address, phone number, name of the psychiatrist, website, etc.
5. A logo could go into either side of the business card. Let's see what looks better.

```html
<!DOCTYPE html>
<html lang="en">
<head>
<meta charset="utf-8">
<title>Brynmoor Family Psychiatry – Business Card</title>
<link href="https://fonts.googleapis.com/css2?family=Cinzel:wght@500&family=Open+Sans:wght@400;600&display=swap" rel="stylesheet">
<style>
  :root {
    --backdrop: #2a2a2a;
    --card-light: #efefef;
    --brand-blue: #29a8e0;
    --ink: #1c1c1c;
    --rule: #a9a9a9;
    --white: #ffffff;
  }
  html, body {
    margin: 0;
    width: 1200px;
    height: 1200px;
    overflow: hidden;
    background: var(--backdrop);
  }
  .card {
    position: absolute;
    top: 310px;
    width: 364px;
    height: 594px;
    box-sizing: border-box;
    text-align: center;
    font-family: "Open Sans", Arial, sans-serif;
  }
  .card--front { left: 234px; background: var(--card-light); }
  .card--back { left: 628px; width: 368px; background: var(--brand-blue); }

  .brand-dot {
    position: absolute;
    left: 50%;
    top: 86px;
    width: 64px;
    height: 64px;
    margin-left: -32px;
    border-radius: 50%;
    background: var(--brand-blue);
  }
  .brand-name {
    position: absolute;
    left: 0;
    right: 0;
    font-family: "Cinzel", Georgia, serif;
    font-weight: 500;
    line-height: 1.15;
    letter-spacing: 0.04em;
  }
  .card--front .brand-name { top: 196px; font-size: 34px; color: var(--brand-blue); }
  .card--back .brand-name { top: 418px; font-size: 34px; color: var(--white); }

  .contact {
    position: absolute;
    left: 0;
    right: 0;
    top: 343px;
    color: var(--ink);
  }
  .contact__name {
    font-family: "Cinzel", Georgia, serif;
    font-weight: 500;
    font-size: 23px;
    color: var(--brand-blue);
    margin: 0;
    line-height: 1.1;
  }
  .contact__role { font-size: 17px; margin: 0; line-height: 1.3; }
  .contact__rule {
    width: 208px;
    height: 1px;
    background: var(--rule);
    margin: 11px auto 10px;
    border: 0;
  }
  .contact__lines { font-size: 17px; line-height: 21.5px; margin: 0; }
  .label { color: var(--brand-blue); }
  .web { color: var(--brand-blue); font-weight: 600; }

  .back-url {
    position: absolute;
    left: 0;
    right: 0;
    top: 520px;
    font-size: 17px;
    font-weight: 600;
    color: var(--white);
  }
</style>
</head>
<body>
  <section class="card card--front">
    <div class="brand-dot"></div>
    <div class="brand-name">Brynmoor<br>Family Psychiatry</div>

    <div class="contact">
      <p class="contact__name">Daniel Hartwell</p>
      <p class="contact__role">Managing Director</p>
      <hr class="contact__rule">
      <p class="contact__lines">
        <span class="label">P:</span> 044-555 210 347<br>
        <span class="label">M:</span> 044-555 210 347<br>
        <span class="label">E:</span> hello@brynmoor.com<br>
        <span class="web">www.brynmoorfp.com</span>
      </p>
      <hr class="contact__rule">
      <p class="contact__lines">
        48 Larchfield Road, Suite 2<br>
        Westbury, 204816.
      </p>
    </div>
  </section>

  <section class="card card--back">
    <div class="brand-name">Brynmoor<br>Family Psychiatry</div>
    <div class="back-url">www.brynmoorfp.com</div>
  </section>
</body>
</html>
```